Up to the Challenge? Canadian based consulting company needs a two sided business card design

A Canadian based security risk management consulting company needs a two-sided business card design. What we do is provide advice and guidance related to emergency, security and business continuity management for small, medium and large companies to help ensure the protection of their people, assets, information, services, operations and reputation.

The final design should be simple, only one or two colours, eye catching, professional and one that makes people look at three or more times just because it looks so darn good.

I have include examples of business cards I like.

Target Market(s)

Small, medium and large companies.

Industry/Entity Type

Security

Contact Information for Business Card

Business Card Size: Standard size of 3.5" (89mm) x 2.0" (51mm) - (see full specifications and guides on PRINTA's website if required)
Card Stock: Looking to use PRINTA's Velda 32pt stock textured paper - seam colour either chili red or black
Business Name: The Harrowfield Group
Website: www.theharrowfieldgroup.example
Telephone: (555)214-0397
Name: Dana Forsythe
Position: Principle
e-mail: Dana.Forsythe@theharrowfieldgroup.example

Font styles to use
Serif

Colors
ec1f27
000000
9d9d9d
aaaaaa
606060

Requirements
Must have
• - "The Harrowfield Group" logo (see uploaded files). I have included grey scale and colour versions.
• - Business card details (as above)
Nice to have
• - One side black or grey scale.
• - Other side would likely be white.
• - Everyone likes the silver logo on the black background.
• - Small element of colour i.e. red but I'm leaning more to greyscale.
Should not have
• - A lot of colour. Keep it simple.

```html
<!DOCTYPE html>
<html lang="en">
<head>
<meta charset="utf-8">
<title>The Harrowfield Group – Business Card</title>
<link rel="stylesheet" href="https://fonts.googleapis.com/css2?family=Cinzel:wght@400;500&family=Oswald:wght@500;600&family=Source+Sans+3:wght@400;500&display=swap">
<style>
  :root {
    --red: #ec1f27;
    --black: #000000;
    --ink: #111111;
    --card-dark: #1a1a1a;
    --card-dark-edge: #060606;
    --silver: #9d9d9d;
    --silver-light: #aaaaaa;
    --grey-mid: #606060;
    --paper: #ffffff;
    --page: #efefef;
    --ghost: rgba(0, 0, 0, 0.06);
  }
  * { box-sizing: border-box; margin: 0; padding: 0; }
  html, body {
    width: 1200px; height: 1111px; overflow: hidden;
    background: var(--page);
  }
  .sheet { position: relative; width: 1200px; height: 1111px; }
  .card {
    position: absolute; left: 160px; width: 880px; height: 503px;
    overflow: hidden;
    box-shadow: 0 6px 18px rgba(0,0,0,0.18);
  }
  .card--front { top: 35px; background: var(--card-dark); }
  .card--back { top: 573px; background: var(--paper); }

  /* Front */
  .front-texture {
    position: absolute; inset: 0;
    background: radial-gradient(ellipse at 50% 45%, #3a3a3a 0%, #202020 45%, var(--card-dark-edge) 100%);
  }
  .brand {
    position: absolute; left: 0; right: 0;
    display: flex; flex-direction: column; align-items: center;
    font-family: "Cinzel", Georgia, serif; color: var(--silver);
  }
  .brand--front { top: 150px; }
  .brand__mark { width: 84px; height: 84px; background: var(--grey-mid); margin-bottom: 26px; }
  .brand__name { font-size: 38px; font-weight: 500; letter-spacing: 1px; line-height: 1; white-space: nowrap; }
  .brand__sub { font-size: 24px; letter-spacing: 8px; line-height: 1; margin-top: 6px; }

  /* Back */
  .ghost-name {
    position: absolute; left: 260px; top: 352px;
    font-family: "Cinzel", Georgia, serif; font-size: 68px; color: var(--ghost);
    white-space: nowrap; letter-spacing: 2px;
  }
  .ghost-mark { position: absolute; left: 380px; top: 150px; width: 120px; height: 120px; background: var(--ghost); }
  .wedge { position: absolute; inset: 0; }
  .brand--back { top: 152px; left: 560px; right: 10px; }
  .brand--back .brand__mark { width: 36px; height: 36px; margin-bottom: 10px; }
  .brand--back .brand__name { font-size: 19px; }
  .brand--back .brand__sub { font-size: 13px; letter-spacing: 4px; margin-top: 2px; }

  .holder { position: absolute; left: 70px; top: 56px; }
  .holder__name {
    font-family: "Oswald", "Arial Narrow", sans-serif; font-weight: 600;
    font-size: 46px; line-height: 1; color: var(--ink); letter-spacing: -0.5px;
  }
  .holder__role {
    font-family: "Source Sans 3", Arial, sans-serif; font-size: 24px;
    color: var(--ink); margin: 6px 0 0 60px;
  }
  .contacts { position: absolute; left: 88px; top: 236px; list-style: none; }
  .contacts__item {
    display: flex; align-items: center; height: 48px;
    font-family: "Source Sans 3", Arial, sans-serif; font-weight: 500;
    font-size: 23px; color: var(--ink);
  }
  .contacts__icon { width: 22px; height: 22px; margin-right: 30px; flex: none; }
  .contacts__square { width: 16px; height: 16px; background: var(--red); margin: 0 33px 0 3px; flex: none; }
</style>
</head>
<body>
<main class="sheet">

  <section class="card card--front" aria-label="Card front">
    <div class="front-texture" role="img" aria-label="Dark faceted triangle pattern background"></div>
    <div class="brand brand--front">
      <div class="brand__mark"></div>
      <div class="brand__name">THE HARROWFIELD</div>
      <div class="brand__sub">GROUP</div>
    </div>
  </section>

  <section class="card card--back" aria-label="Card back">
    <div class="ghost-mark"></div>
    <div class="ghost-name">HARROWFIELD</div>

    <svg class="wedge" width="880" height="503" viewBox="0 0 880 503">
      <polygon points="424,176 880,34 880,388" fill="#222222"/>
      <polyline points="880,34 424,176 880,388" fill="none" stroke="var(--red)" stroke-width="2.5"/>
    </svg>

    <div class="brand brand--back">
      <div class="brand__mark"></div>
      <div class="brand__name">THE HARROWFIELD</div>
      <div class="brand__sub">GROUP</div>
    </div>

    <header class="holder">
      <h1 class="holder__name">Dana Forsythe</h1>
      <p class="holder__role">Principle</p>
    </header>

    <ul class="contacts">
      <li class="contacts__item">
        <svg class="contacts__icon" viewBox="0 0 24 24"><path d="M6.6 3.5l3 3.4-1.8 2.3c1.2 2.6 3.2 4.7 5.8 5.9l2.3-1.8 3.4 3-1.8 3.2C10.6 19.200 4.700 13.300 3.400 5.300z" fill="var(--red)"/></svg>
        <span>(555)214-0397</span>
      </li>
      <li class="contacts__item">
        <svg class="contacts__icon" viewBox="0 0 24 24"><rect x="3" y="6" width="18" height="12" fill="none" stroke="var(--red)" stroke-width="2"/><polyline points="3,6 12,13 21,6" fill="none" stroke="var(--red)" stroke-width="2"/></svg>
        <span>Dana.Forsythe@theharrowfieldgroup.example</span>
      </li>
      <li class="contacts__item">
        <svg class="contacts__icon" viewBox="0 0 24 24"><g fill="none" stroke="var(--red)" stroke-width="1.5"><circle cx="12" cy="12" r="9"/><ellipse cx="12" cy="12" rx="4" ry="9"/><line x1="3" y1="12" x2="21" y2="12"/><line x1="5" y1="7" x2="19" y2="7"/><line x1="5" y1="17" x2="19" y2="17"/></g></svg>
        <span>www.theharrowfieldgroup.example</span>
      </li>
      <li class="contacts__item">
        <span class="contacts__square"></span>
        <span>https://ca.profilenet.example/in/danaforsythe</span>
      </li>
    </ul>
  </section>

</main>
</body>
</html>
```